Equipment Finance Specialist I work with companies who need the funds to buy their equipment

I would like a business card that stands out on the shelves. I want to be able to hand it to someone and say WOW. This card should have my logo.
You can put color into it I am very open on design and color

What my company does is we deal with dealerships that sell equipment such as Dump Trucks garbage trucks tractors trailers. Customers get referred to us and depending on their time in business we will ask for the following items

Companies that have been in business for more than two years we have a credit application program up to 250K . With this program we need the following items Credit application filled out(which is what I would like to be able for the customer to click on my website to get.) as well as three current month bank statements.

Deals over 250k we will need the following items

2 years business tax returns
2 years personal tax returns
Profit & Loss statement
Personal Financial Statement

what we do
100% FINANCING
SEASONAL PAYMENTS
LOAN BALLOON PAYMENTS
TRAC LEASING
LOW-INTEREST REFINANCING RATES
DEBT CONSOLIDATION

We specialize in creative financing solutions and offer a variety of reliable, flexible and expandable lending choices.

Target Market(s)

Trucking Companies

Industry/Entity Type

Trucking Company

Contact Information for Business Card

* $250,000 Application only Program
* Loans from $30,000 to 5,000,000
* Competitive Interest Rates

Font styles to use
Serif
Sans Serif

Colors

Designer to choose colors to be used in the design.

Requirements
Must have
• On the back of the card.
• * $250,000 Application only Program
• * Loans from $30,000 to 5,000,000
• My name, email, website. address
• * Competitive Interest Rates
• * 100% Financing
Nice to have
• I want my logo to pop on the card
• My logo is the great one I would like to use
Should not have
• I am up for your creativity as well

```html
<!DOCTYPE html>
<html lang="en">
<head>
<meta charset="utf-8">
<title>Ridgeline Funding – Business Card</title>
<link href="https://fonts.googleapis.com/css2?family=Archivo+Black&family=Open+Sans:wght@400;600&display=swap" rel="stylesheet">
<style>
  :root {
    --navy: #1f2f66;
    --red: #e0202e;
    --white: #ffffff;
    --ink: #1b2140;
    --bg: #4a4b4f;
    --faint-navy: rgba(255,255,255,0.06);
    --faint-grey: #e9eaf0;
  }
  * { box-sizing: border-box; margin: 0; padding: 0; }
  html, body { width: 1200px; height: 880px; overflow: hidden; }
  body {
    background: var(--bg);
    font-family: "Open Sans", sans-serif;
    position: relative;
  }
  .card {
    position: absolute;
    width: 560px;
    height: 330px;
    border-radius: 26px;
    overflow: hidden;
  }
  /* Back card */
  .card-back {
    left: 70px; top: 90px;
    background: var(--navy);
    color: var(--white);
    border-bottom: 8px solid var(--red);
  }
  .card-back .crane-art {
    position: absolute; left: 40px; top: 30px;
    width: 230px; height: 200px;
    background: linear-gradient(135deg, var(--faint-navy), rgba(255,255,255,0.02));
    border-radius: 12px;
  }
  .brand {
    position: absolute;
    display: flex; align-items: center; gap: 14px;
  }
  .brand-dot {
    width: 74px; height: 74px; border-radius: 50%;
  }
  .brand-name {
    font-family: "Archivo Black", sans-serif;
    font-size: 40px; line-height: 0.95;
    letter-spacing: 1px;
    text-transform: uppercase;
  }
  .card-back .brand { left: 150px; top: 70px; }
  .card-back .brand-dot { background: var(--white); }
  .card-back .brand-name { color: var(--white); }
  .card-back .rule {
    position: absolute; left: 40px; right: 40px; top: 210px;
    height: 1px; background: rgba(255,255,255,0.55);
  }
  .features {
    position: absolute; left: 40px; right: 40px; top: 228px;
    display: grid; grid-template-columns: 1fr 1fr;
    row-gap: 8px; column-gap: 20px;
    list-style: none; font-size: 15px;
  }
  .features li::before {
    content: ""; display: inline-block;
    width: 8px; height: 8px; border-radius: 50%;
    background: var(--red); margin-right: 9px; vertical-align: middle;
  }
  /* Front card */
  .card-front {
    left: 570px; top: 470px;
    background: var(--white);
    color: var(--ink);
  }
  .card-front .truck-art {
    position: absolute; left: 20px; top: 60px;
    width: 230px; height: 200px;
    background: var(--faint-grey);
    border-radius: 50%;
  }
  .person {
    position: absolute; right: 36px; top: 28px; text-align: right;
  }
  .person-name {
    font-family: "Archivo Black", sans-serif;
    font-size: 28px; color: var(--navy); letter-spacing: 0.5px;
  }
  .person-role { font-size: 15px; color: var(--red); font-weight: 600; }
  .card-front .brand { left: 170px; top: 120px; }
  .card-front .brand-dot { background: var(--navy); }
  .card-front .brand-name { color: var(--navy); }
  .contacts {
    position: absolute; left: 34px; bottom: 36px;
    list-style: none; font-size: 15px; line-height: 1.75;
  }
  .contacts li { display: flex; align-items: center; gap: 10px; }
  .contacts svg { width: 15px; height: 15px; fill: var(--red); }
  .address {
    position: absolute; right: 34px; bottom: 54px;
    text-align: right; font-size: 15px; line-height: 1.5;
  }
  .front-stripe {
    position: absolute; left: 0; bottom: 0; width: 100%; height: 12px;
  }
</style>
</head>
<body>

<section class="card card-back">
  <div class="crane-art" role="img" aria-label="Faint crane illustration"></div>
  <div class="brand">
    <span class="brand-dot"></span>
    <span class="brand-name">Ridgeline<br>Funding</span>
  </div>
  <div class="rule"></div>
  <ul class="features">
    <li>$250,000 Application only Program</li>
    <li>Loans from $30,000 to 5,000,000</li>
    <li>Competitive Interest Rates</li>
    <li>100% Financing</li>
  </ul>
</section>

<section class="card card-front">
  <div class="truck-art" role="img" aria-label="Faint dump truck illustration"></div>
  <div class="person">
    <div class="person-name">DANIEL REYES</div>
    <div class="person-role">Founder &amp; CEO</div>
  </div>
  <div class="brand">
    <span class="brand-dot"></span>
    <span class="brand-name">Ridgeline<br>Funding</span>
  </div>
  <ul class="contacts">
    <li><svg viewBox="0 0 24 24"><path d="M6.6 10.8a15 15 0 0 0 6.6 6.6l2.2-2.2c.3-.3.7-.4 1-.2 1.1.4 2.3.6 3.6.6.6 0 1 .4 1 1V20c0 .6-.4 1-1 1A17 17 0 0 1 3 4c0-.6.4-1 1-1h3.5c.6 0 1 .4 1 1 0 1.3.2 2.5.6 3.6.1.3 0 .7-.2 1z"/></svg>555 014 2270</li>
    <li><svg viewBox="0 0 24 24"><path d="M2 5h20v14H2z M2 5l10 8 10-8" /></svg>info@ridgelinefunding.com</li>
    <li><svg viewBox="0 0 24 24"><circle cx="12" cy="12" r="10"/></svg>www.ridgelinefunding.com</li>
  </ul>
  <div class="address">48 Harbour Lane<br>Suite B, Leeds, UK LS1 4QT</div>
  <svg class="front-stripe" viewBox="0 0 560 12" preserveAspectRatio="none">
    <rect x="0" y="0" width="560" height="12" fill="#1f2f66"/>
    <polygon points="440,0 560,0 560,12 432,12" fill="#e0202e"/>
  </svg>
</section>

</body>
</html>
```